Lumen Harbor Business Card Design Project

We have recently rebranded and would like to design new business cards that incorporate the corporate logo - double sided cards with corporate logo on one side and contact details on the other

Target Market(s)

Sophisticated and high net worth investors and finance industry professionals

Industry/Entity Type

Funds Management

Contact Information for Business Card

The card should prominently feature the company name and logo. Other details will be standard contact details for each staff member - name, address, phone, email, website

Colors
0054AA
0677BA
7BADD7
CADEEF
E8F1F8

Requirements
Must have
• Double-sided design with one side prominently featuring the corporate logo and the other side with all standard contact details

```html
<!DOCTYPE html>
<html lang="en">
<head>
<meta charset="utf-8">
<title>Lumen Harbor – Business Card</title>
<link rel="stylesheet" href="https://fonts.googleapis.com/css2?family=Jost:wght@400;500;600&display=swap">
<style>
  :root {
    --backdrop: #e4e4e2;
    --paper: #ffffff;
    --navy: #1f4677;
    --navy-deep: #15223d;
    --navy-mid: #1d3a66;
    --ink-light: #ffffff;
    --shadow: rgba(0, 0, 0, 0.18);
  }
  * { margin: 0; padding: 0; box-sizing: border-box; }
  html, body {
    width: 1200px; height: 846px; overflow: hidden;
    background: var(--backdrop);
    font-family: "Jost", "Futura", sans-serif;
  }
  .canvas { position: relative; width: 1200px; height: 846px; }

  .card {
    position: absolute; left: 346px; width: 508px; height: 290px;
    box-shadow: 14px 14px 18px var(--shadow);
    overflow: hidden;
  }
  .card--front { top: 99px; background: var(--paper); color: var(--navy); }
  .card--back { top: 456px; background: var(--navy-deep); }

  .holder-name {
    position: absolute; left: 40px; top: 37px;
    font-size: 19px; font-weight: 600; letter-spacing: 0.2px;
  }

  .contact-list {
    position: absolute; right: 40px; top: 40px;
    list-style: none; text-align: right;
    font-size: 12.5px; font-weight: 400; line-height: 17.5px;
  }
  .contact-list li { display: flex; justify-content: flex-end; align-items: center; gap: 7px; }
  .contact-list svg { width: 14px; height: 14px; fill: var(--navy); flex: none; }

  .wordmark {
    position: absolute; display: flex; align-items: center; gap: 12px;
    font-weight: 500; text-transform: uppercase; letter-spacing: 2px; white-space: nowrap;
  }
  .wordmark__dot { border-radius: 50%; flex: none; }
  .card--front .wordmark {
    right: 40px; top: 154px; font-size: 36px; color: var(--navy);
  }
  .card--front .wordmark__dot { width: 30px; height: 30px; background: var(--navy); }

  .address-band {
    position: absolute; left: 0; right: 0; top: 237px; height: 31px;
    background: var(--navy); color: var(--ink-light);
    font-size: 12px; display: flex; align-items: center; justify-content: flex-end;
    padding-right: 41px; letter-spacing: 0.2px;
  }

  .back-photo {
    position: absolute; inset: 0;
    background:
      linear-gradient(118deg, transparent 0 28%, rgba(40, 80, 140, 0.35) 30%, transparent 38%,
                      transparent 48%, rgba(40, 80, 140, 0.3) 50%, transparent 56%),
      linear-gradient(90deg, rgba(38, 72, 125, 0.55) 0%, rgba(21, 34, 61, 0) 22%),
      var(--navy-deep);
  }
  .card--back .wordmark {
    left: 50%; top: 50%; transform: translate(-50%, -50%);
    font-size: 40px; color: var(--ink-light);
  }
  .card--back .wordmark__dot { width: 32px; height: 32px; background: var(--ink-light); }
</style>
</head>
<body>
<main class="canvas">

  <section class="card card--front" aria-label="Card front with contact details">
    <h1 class="holder-name">Nina Castell</h1>

    <ul class="contact-list">
      <li>+02 9400 5517
        <svg viewBox="0 0 24 24" aria-hidden="true"><path d="M6.6 2.5c.6-.4 1.4-.2 1.8.4l2 3.4c.3.6.2 1.3-.3 1.7l-1.6 1.2c.9 2.3 2.3 4.3 4.3 5.9l1.6-1.1c.5-.4 1.3-.3 1.7.2l2.5 3c.4.5.4 1.3-.1 1.8l-1.6 1.5c-1 .9-2.5 1.1-3.7.4C8 18.7 4.6 13.8 3.6 8.2c-.2-1.3.3-2.6 1.3-3.4z"/></svg>
      </li>
      <li>nina.castell@lumen-harbor.com
        <svg viewBox="0 0 24 24" aria-hidden="true"><path d="M2 5h20v14H2z M3.5 6.5v.4l8.5 6.3 8.5-6.3v-.4z M3.5 8.8v8.7h17V8.8l-8.5 6.2z"/></svg>
      </li>
      <li>www.lumen-harbor.com
        <svg viewBox="0 0 24 24" aria-hidden="true"><circle cx="12" cy="12" r="10"/><path d="M2 12h20M12 2v20M12 2c-3.5 3-3.5 17 0 20M12 2c3.5 3 3.5 17 0 20M4 7h16M4 17h16" stroke="#fff" stroke-width="1.2" fill="none"/></svg>
      </li>
    </ul>

    <div class="wordmark"><span class="wordmark__dot"></span>Lumen Harbor</div>

    <p class="address-band">Level 14 Meridian House, 40 Keel Street, Sydney NSW 2000</p>
  </section>

  <section class="card card--back" aria-label="Card back with company name">
    <div class="back-photo" role="img" aria-label="Dark blue toned photograph of classical stone columns"></div>
    <div class="wordmark"><span class="wordmark__dot"></span>Lumen Harbor</div>
  </section>

</main>
</body>
</html>
```